Brochure Design Project / IT Consulting Firm

We need a brochure for a IT consulting firm based in Chile.
We are the subsidiary of a french based multinational (www.groupe-vorlen.example).
Our purpose is to solve our customers IT needs, while our vision is to become the premier IT company in Chile.
We delivery basically three types of services:
- software development
- system integration
- consulting
The brochure must be:
- innovative (not the classical boring IT consulting firm with the handshaking stock image in the cover)
- clear and concise designed
Website: http://www.pkmarsa.example
Headquarter website: http://www.groupe-vorlen.example
Chilean recruiting blog: http://sumatebrovel.example
Files added:
- powerpoint file with our corporate presentation (is in Spanish).
- psd and png with our logo
- sample design of a folder we did
Note:
- maybe not all the content of the ppt will be put into the brochure, it should serve as an idea of the content that we should have inside
- we may create different version with different contents of the same brochure, for different services/markets we serve
Target Market(s)
CxO and managers
Industry/Entity Type
Software
Look and feel
Each slider illustrates characteristics of the customer's brand and the style your logo design should communicate.

```html
<!DOCTYPE html>
<html lang="es">
<head>
<meta charset="utf-8">
<title>Pkmarsa Chile – Folleto</title>
<link href="https://fonts.googleapis.com/css2?family=Exo:ital,wght@0,600;0,700;0,800;1,700&family=Open+Sans:ital,wght@0,400;0,600;0,700;1,400&display=swap" rel="stylesheet">
<style>
:root{
  --backdrop:#2b2b2d;
  --navy:#1c3a5e;
  --navy-deep:#142c4a;
  --red:#d8262e;
  --orange:#f39a1e;
  --ink:#3b4756;
  --muted:#5d6a78;
  --white:#ffffff;
  --heading:"Exo", sans-serif;
  --body:"Open Sans", sans-serif;
}
*{margin:0;padding:0;box-sizing:border-box}
html,body{width:855px;height:1200px;overflow:hidden;background:var(--backdrop)}
.canvas{position:relative;width:855px;height:1200px}

/* inside spread */
.spread{position:absolute;left:20px;top:24px;width:815px;height:548px;background:var(--white);overflow:hidden;font-family:var(--body);color:var(--ink)}
.spread-art{position:absolute;inset:0}
.block{position:absolute}
.block h2{font-family:var(--heading);font-weight:700;color:var(--navy);font-size:13px;letter-spacing:.3px;margin-bottom:5px;line-height:1.15}
.block h3{font-family:var(--heading);font-weight:700;color:var(--navy);font-size:8px;margin:6px 0 2px}
.block p{font-size:6.2px;line-height:1.45;margin-bottom:5px;color:var(--muted)}
.facts{list-style:none;font-size:6px;line-height:1.45;color:var(--muted)}
.facts li::before{content:"";display:inline-block;width:4px;height:4px;background:var(--navy);margin-right:4px;vertical-align:middle}
.about{left:16px;top:14px;width:182px}
.model{left:212px;top:14px;width:168px}
.services{margin-top:6px;background:var(--orange);border-radius:7px;padding:12px 12px 10px}
.services h4{font-family:var(--heading);font-weight:700;color:var(--white);font-size:8px;line-height:1.25;margin-bottom:7px;text-transform:uppercase}
.services ul{list-style:none;margin-top:8px}
.services li{color:var(--white);font-size:6.6px;line-height:1.3;margin-bottom:3px;opacity:.92}
.services li::before{content:"– "}

.skills{left:408px;top:14px;width:396px;color:var(--white)}
.skills h2{color:var(--white);font-size:13px}
.skill-cols{display:flex;gap:12px}
.skill-col{flex:1}
.skills h3{color:var(--white);font-size:7.5px;text-transform:uppercase;margin:3px 0 3px}
.skills p{color:#dbe4ef;font-size:5.6px;line-height:1.4;margin-bottom:3px}
.skills b{color:var(--white);font-weight:700}

.commit-title{position:absolute;left:28px;top:372px;font-family:var(--heading);font-style:italic;font-weight:700;color:var(--white);font-size:14px;letter-spacing:.5px;transform:rotate(-4deg)}
.tab{position:absolute;width:40px;height:24px;background:var(--white);font-family:var(--heading);font-weight:800;font-size:13px;color:var(--navy);display:flex;align-items:center;justify-content:center;border-radius:2px}
.pledges{position:absolute;left:10px;top:452px;width:800px;display:flex;gap:8px}
.pledge{flex:1}
.pledge h4{font-family:var(--heading);font-weight:700;color:var(--red);font-size:7.5px;margin-bottom:2px;text-transform:uppercase}
.pledge p{font-size:5.8px;line-height:1.45;color:var(--muted)}

/* covers */
.cover{position:absolute;top:600px;width:300px;height:420px;overflow:hidden}
.front{left:100px;background:var(--white)}
.back{left:455px;background:var(--navy)}
.cover svg{position:absolute;inset:0}
.brand{position:absolute;font-family:var(--heading);font-weight:700;letter-spacing:.5px}
.front .brand{left:28px;top:378px;font-size:17px;color:var(--muted)}
.back .brand{left:0;right:0;top:134px;text-align:center;font-size:26px;color:var(--white)}
.contact{position:absolute;left:160px;top:334px;width:120px;text-align:center;font-family:var(--body);font-style:italic;font-size:6.8px;line-height:1.6;color:#dbe4ef}
.contact strong{font-style:normal;color:var(--white)}
</style>
</head>
<body>
<main class="canvas">

  <section class="spread" aria-label="Interior del folleto">
    <svg class="spread-art" viewBox="0 0 815 548">
      <defs>
        <linearGradient id="bandPhoto" x1="0" y1="0" x2="1" y2="0">
          <stop offset="0" stop-color="#3f5f8f"/>
          <stop offset=".35" stop-color="#8fa6c4"/>
          <stop offset=".6" stop-color="#5d7fae"/>
          <stop offset="1" stop-color="#9fc0d8"/>
        </linearGradient>
      </defs>
      <path d="M394 0H815V250C700 290 560 300 394 318Z" fill="var(--navy)"/>
      <path d="M394 300C560 285 700 270 815 225V245C700 285 560 298 394 314Z" fill="var(--red)"/>
      <g role="img" aria-label="Fotografía: globo terráqueo con direcciones web y piezas de rompecabezas con la palabra solución">
        <path d="M0 352C220 330 520 330 815 240V360C600 420 300 418 0 420Z" fill="url(#bandPhoto)"/>
      </g>
      <path d="M0 352C160 338 300 336 430 340V352C300 350 160 356 0 372Z" fill="var(--navy)" opacity=".9"/>
      <path d="M0 402C300 400 600 400 815 345V356C600 410 300 414 0 416Z" fill="var(--red)"/>
      <path d="M0 416C300 414 600 410 815 356V372C600 424 300 430 0 432Z" fill="var(--navy-deep)"/>
    </svg>

    <div class="block about">
      <h2>QUIÉNES SOMOS</h2>
      <p>Pkmarsa Chile es un proveedor de servicios de ingeniería multinacional, que presta soluciones de valor añadido y proyectos de tecnología de la información y comunicación a las principales empresas del mundo y contribuye al desarrollo de las tecnologías más innovadoras y avanzadas.</p>
      <p>Nuestra estrategia de crecimiento es simple: ofrecer los mejores consultores, entregar proyectos de éxito, y hacer que nuestra reputación nos preceda.</p>
      <h3>GRUPO VORLEN (desde 1979):</h3>
      <ul class="facts">
        <li>4.000 ingenieros en 12 países</li>
        <li>Empresa cotizada en bolsa europea desde 1999</li>
        <li>Ingresos en 2010: 222,1 M. EUR; Equity: 53 M. EUR</li>
      </ul>
      <h3>Pkmarsa Chile – Grupo Vorlen (desde 2010):</h3>
      <ul class="facts">
        <li>35 ingenieros en Santiago</li>
        <li>Trabajando para 12 grandes clientes</li>
        <li>Entre las compañías de mayor crecimiento en Chile</li>
        <li>Ingresos estimados 2011: 1.100 Millones de CLP</li>
      </ul>
      <h2 style="margin-top:9px">SECTORES</h2>
      <p>Muchas medianas y grandes compañías de diferentes sectores ya han depositado su confianza en los servicios ofrecidos por Pkmarsa. Nuestros servicios son flexibles y se adaptan para proporcionar las mejores soluciones para nuestros clientes.</p>
    </div>

    <div class="block model">
      <h2>MODELO DE COLABORACIÓN</h2>
      <p>Pkmarsa ofrece servicios de alta calidad en el campo de las Tecnologías de la Información y Comunicación (TIC). Presente hace dos años en Chile, nos respaldan los más de 30 años de experiencia y conocimientos acumulados del grupo en Europa y en el mundo. Ofrecemos servicios de asesoramiento y consultoría, gestión de infraestructuras, desarrollo de software, así como la integración y el mantenimiento de sistemas informáticos en diferentes modelos de colaboración, ajustados a las expectativas y exigencias de nuestros clientes.</p>
      <div class="services">
        <h4>Desarrollo de aplicaciones integración de sistemas &amp; mantención</h4>
        <h4>Infraestructura y seguridad informática</h4>
        <h4>Consultoría en ingeniería</h4>
        <ul>
          <li>Staffing / Outsourcing / Asistencia Técnica de Ingenieros TIC</li>
          <li>Team Leasing</li>
          <li>Proyectos Llave en Mano</li>
          <li>Service management / Gestión de Proyectos y Programas / Consulting</li>
        </ul>
      </div>
    </div>

    <div class="block skills">
      <h2>COMPETENCIAS</h2>
      <div class="skill-cols">
        <div class="skill-col">
          <h3>Desarrollo de software</h3>
          <p><b>Programación:</b> lenguajes orientados a objetos, funcionales, scripting y sistemas heredados.</p>
          <p><b>Web:</b> portales, servicios web, aplicaciones ricas y arquitecturas orientadas a servicios.</p>
          <p><b>Bases de datos:</b> motores relacionales, modelado, consultas y optimización.</p>
          <p><b>Servidores de aplicaciones:</b> plataformas empresariales y contenedores ligeros.</p>
          <h3>Consultoría e ingeniería</h3>
          <p><b>Sistemas embebidos y tiempo real:</b> sistemas operativos de tiempo real y microcontroladores.</p>
          <p><b>Electrónica:</b> circuitos integrados, lógica programable y diseño digital.</p>
          <p><b>Telecom:</b> redes móviles, inalámbricas, telefonía IP y redes inteligentes.</p>
          <p><b>Movilidad:</b> aplicaciones para teléfonos inteligentes y dispositivos portátiles.</p>
        </div>
        <div class="skill-col">
          <p><b>Mecánica:</b> diseño asistido, termodinámica, mecánica de fluidos y simulación.</p>
          <h3>Aplicaciones y plataformas</h3>
          <p><b>ERP:</b> planificación de recursos y gestión financiera.</p>
          <p><b>CRM:</b> gestión de clientes y automatización comercial.</p>
          <p><b>Inteligencia de negocio:</b> almacenes de datos, procesos de carga, minería de datos e informes.</p>
          <p><b>Integración:</b> servicios web, buses de integración y mensajería.</p>
          <p><b>Gestión de contenidos:</b> portales colaborativos y gestión documental.</p>
        </div>
        <div class="skill-col">
          <h3>Sistemas e infraestructuras</h3>
          <p><b>Administración de sistemas:</b> servidores de distintos sistemas operativos y virtualización.</p>
          <p><b>Arquitectura de redes:</b> redes locales y extendidas, enrutadores, conmutadores, directorios y correo.</p>
          <p><b>Administración de bases de datos:</b> instalación, respaldo y rendimiento.</p>
          <p><b>Soporte TI:</b> mesa de ayuda, marcos de buenas prácticas y gobierno TI.</p>
        </div>
      </div>
    </div>

    <div class="commit-title">NUESTRO COMPROMISO</div>
    <div class="tab" style="left:20px;top:424px">01</div>
    <div class="tab" style="left:156px;top:422px">02</div>
    <div class="tab" style="left:278px;top:420px">03</div>
    <div class="tab" style="left:425px;top:414px">04</div>
    <div class="tab" style="left:547px;top:404px">05</div>
    <div class="tab" style="left:700px;top:392px">06</div>

    <div class="pledges">
      <article class="pledge"><h4>La competencia</h4><p>Un proceso riguroso de selección, acciones formativas adaptadas a las exigencias del mercado y profesionales capacitados nos permiten ofrecer un perfecto nivel en cada actividad.</p></article>
      <article class="pledge"><h4>La escucha</h4><p>Su satisfacción depende en primer lugar de la calidad de nuestra escucha. Entendemos sus necesidades para responder con precisión.</p></article>
      <article class="pledge"><h4>El consejo</h4><p>Para responder a sus necesidades, establecemos un proceso técnico que nos conduce a proponer la mejor solución.</p></article>
      <article class="pledge"><h4>Los plazos</h4><p>En constante búsqueda de elementos innovadores, garantizamos los últimos avances tecnológicos en nuestras acciones, avaladas por planes de formación y nuestros conocimientos.</p></article>
      <article class="pledge"><h4>El futuro</h4><p>En constante búsqueda de elementos innovadores, garantizamos los últimos avances tecnológicos en nuestras acciones, avalada por nuestros planes de formación y responde a nuestro objetivo de capitalización de conocimientos.</p></article>
      <article class="pledge"><h4>El servicio</h4><p>Proponemos prestaciones atendiendo a sus exigencias. Nuestro servicio garantiza un total respaldo y asesoramiento a largo plazo, ofreciendo lo mejor en cada momento.</p></article>
    </div>
  </section>

  <section class="cover front" aria-label="Portada">
    <svg viewBox="0 0 300 420">
      <defs>
        <radialGradient id="coverPhoto" cx=".45" cy=".55" r=".75">
          <stop offset="0" stop-color="#ff9ad0"/>
          <stop offset=".35" stop-color="#e8348a"/>
          <stop offset=".75" stop-color="#c9202e"/>
          <stop offset="1" stop-color="#e8702a"/>
        </radialGradient>
      </defs>
      <g role="img" aria-label="Ilustración: escalera que asciende sobre un fondo rojo y fucsia con códigos binarios luminosos">
        <path d="M0 0H300V230C200 250 90 290 0 330Z" fill="url(#coverPhoto)"/>
      </g>
      <path d="M0 300C90 262 200 230 300 220V240C200 252 100 282 0 330Z" fill="#c4cbd4"/>
      <path d="M0 318C100 278 200 250 300 240V262C200 270 100 298 0 340Z" fill="var(--navy)"/>
      <path d="M0 340C100 300 200 274 300 262V272C200 282 100 310 0 350Z" fill="var(--red)"/>
      <path d="M0 352C100 316 200 292 300 282" stroke="#a9b2bd" stroke-width="1.2" fill="none"/>
      <path d="M0 360C100 326 200 304 300 294" stroke="#c9cfd6" stroke-width="1" fill="none"/>
    </svg>
    <div class="brand">Pkmarsa</div>
  </section>

  <section class="cover back" aria-label="Contraportada">
    <svg viewBox="0 0 300 420">
      <defs>
        <linearGradient id="backPhoto" x1="0" y1="0" x2="1" y2="0">
          <stop offset="0" stop-color="#5a7cab"/>
          <stop offset=".5" stop-color="#9cb4cf"/>
          <stop offset="1" stop-color="#4e6f9c"/>
        </linearGradient>
      </defs>
      <path d="M0 262C100 255 200 235 300 196V212C200 250 100 270 0 276Z" fill="var(--red)"/>
      <g role="img" aria-label="Fotografía: globo terráqueo con direcciones web y piezas de rompecabezas">
        <path d="M0 276C100 270 200 250 300 212V278C200 300 100 308 0 306Z" fill="url(#backPhoto)"/>
      </g>
      <path d="M0 306C100 308 200 300 300 278V288C200 310 100 318 0 316Z" fill="var(--white)"/>
      <path d="M0 316C100 318 200 310 300 288V294C200 316 100 324 0 322Z" fill="var(--red)"/>
    </svg>
    <div class="brand">Pkmarsa</div>
    <address class="contact">
      Av. Los Almendros 1450<br>
      Código postal 7500000<br>
      Santiago de Chile<br>
      <strong>Teléfono: +56 (0) 22 000 0000</strong><br>
      info@pkmarsa.example<br>
      www.pkmarsa.example
    </address>
  </section>

</main>
</body>
</html>
```